Logo & Website Reference Design for "DuneLoop.Trips"

Hi there!

I like to get a logo, website incl. fonts reference design for "Dune Loop Trips". The URL will be DuneLoop.Trips or Dune-Loop.Trips and would like to have a memorable symbol, too. Basically, the symbol should not be a OffRoad car rather than e.g. Mountains, Trails, skid-marks etc.. The website and activities I will provide video documented of off-road trails with off-road cars; mainly off-road campers and POI's will be mentioned online. Not "extreme Off-Road" folks with their Brask Hollin Vantors or Trellmor Quads rather than more mainstream. It would be great if you could consider Kestelwagen Camper Vans (modern, K4 or K7) that are offroad capable (higher, extreme tires, snorkel etc.).

If you work on the sample images for the website, pls make use of e.g. off-road trails (gravel roads) thru forest, mountains, rocks etc. - no street roads.

Also, I am planning to manage the website content with pagevoro.com - if you have any experience - much appreciated. Alternatively, I am also happy with e.g. SiteQuill to manage the content in the close future on my onwn.

Target Market(s)

Key target audience are mainly male people in Central- Northern- and Benelux Europe in the age of 28 - 55 years.

Industry/Entity Type

Tourism

Logo Text

Dune-Loop.Trips or DuneLoop.Trips (please recommend with "-" or w/o)

Number of Pages Required

4 page

Font styles to use
Sans Serif

Colors

Designer to choose colors to be used in the design.

Requirements
Must have
• Modern and attractive logo with symbol that works w/o text (DuneLoop.Trips).
• Webdesign must work on mobile devices (responsive) as well as on computer browsers
Nice to have
• Even if URL is DuneLoop.Trips and/or Dune-Loop.Trips the sub-slogan could be used e.g. real Dune-Loop Trips | virtual
• Favicon for website

```html
<!DOCTYPE html>
<html lang="en">
<head>
<meta charset="utf-8">
<title>Dune Loop Trips — Website + Logo Design</title>
<link rel="stylesheet" href="https://fonts.googleapis.com/css2?family=Montserrat:wght@300;400;600;800&display=swap">
<style>
  :root {
    --canvas: #ededed;
    --ink: #3a3a3a;
    --caption: #b9b9b9;
    --night-top: #0c1a2c;
    --night-mid: #12304a;
    --ground: #1a1420;
    --van: #8a4a2c;
    --white: #ffffff;
    --green: #3fbf7f;
  }
  * { box-sizing: border-box; margin: 0; padding: 0; }
  html, body { width: 1200px; height: 1200px; overflow: hidden; }
  body {
    background: var(--canvas);
    font-family: "Montserrat", sans-serif;
    color: var(--ink);
    position: relative;
  }

  /* Brand presentation */
  .brand-block {
    position: absolute; top: 96px; left: 0; width: 1200px;
    display: flex; flex-direction: column; align-items: center;
  }
  .brand-lockup { display: flex; align-items: center; gap: 16px; }
  .brand-mark { width: 26px; height: 26px; background: var(--ink); }
  .brand-name {
    font-weight: 600; font-size: 36px; letter-spacing: 3px;
    text-transform: uppercase; color: var(--ink);
  }
  .brand-caption {
    margin-top: 42px; font-size: 14px; letter-spacing: 1.5px;
    text-transform: uppercase; color: var(--caption); font-weight: 400;
  }

  /* Shared hero screen */
  .screen { position: absolute; overflow: hidden; color: var(--white); }
  .hero-photo {
    position: absolute; inset: 0;
    background:
      radial-gradient(ellipse at 72% 82%, rgba(196,102,60,.55), transparent 38%),
      radial-gradient(ellipse at 80% 70%, rgba(150,90,230,.35), transparent 25%),
      linear-gradient(180deg, var(--night-top) 0%, var(--night-mid) 55%, #1b2a2a 72%, var(--ground) 100%);
  }
  .site-header {
    position: absolute; top: 0; left: 0; right: 0;
    display: flex; justify-content: space-between; align-items: center;
  }
  .site-logo { display: flex; align-items: center; gap: 8px; }
  .site-logo .mark { background: var(--white); }
  .site-logo .name { font-weight: 600; text-transform: uppercase; letter-spacing: 1px; }
  .site-nav { display: flex; }
  .site-nav a {
    color: var(--white); text-decoration: none; font-weight: 600;
    text-transform: uppercase; font-size: 11px; letter-spacing: .5px;
  }
  .hero-copy { position: absolute; left: 0; right: 0; text-align: center; }
  .hero-lead { font-weight: 300; text-transform: uppercase; letter-spacing: 1px; }
  .hero-title { font-weight: 800; text-transform: uppercase; letter-spacing: 2px; }
  .btn-book {
    display: inline-flex; align-items: center; gap: 10px;
    background: var(--green); color: var(--white); font-weight: 800;
    text-transform: uppercase; letter-spacing: 1px;
  }

  /* Desktop */
  .screen-desktop { left: 60px; top: 300px; width: 760px; height: 475px; }
  .screen-desktop .site-header { padding: 26px 22px 0 22px; }
  .screen-desktop .mark { width: 16px; height: 16px; }
  .screen-desktop .name { font-size: 17px; }
  .screen-desktop .site-nav { gap: 30px; }
  .screen-desktop .hero-copy { top: 164px; }
  .screen-desktop .hero-lead { font-size: 26px; }
  .screen-desktop .hero-title { font-size: 26px; margin-top: 2px; }
  .screen-desktop .btn-book { margin-top: 26px; padding: 9px 16px; font-size: 13px; }

  /* Mobile */
  .screen-mobile { left: 880px; top: 300px; width: 260px; height: 462px; }
  .screen-mobile .site-header { padding: 14px 14px 0 14px; }
  .screen-mobile .mark { width: 10px; height: 10px; }
  .screen-mobile .name { font-size: 11px; }
  .screen-mobile .menu-toggle { width: 14px; height: 10px; }
  .screen-mobile .hero-copy { top: 130px; padding: 0 18px; }
  .screen-mobile .hero-lead { font-size: 16px; }
  .screen-mobile .hero-title { font-size: 19px; line-height: 1.2; margin-top: 2px; }
  .screen-mobile .btn-book { margin-top: 28px; padding: 7px 14px; font-size: 9px; gap: 6px; }
</style>
</head>
<body>

  <header class="brand-block">
    <div class="brand-lockup">
      <span class="brand-mark"></span>
      <span class="brand-name">Dune-Loop Trips</span>
    </div>
    <p class="brand-caption">Dune Loop Trips website + logo design</p>
  </header>

  <section class="screen screen-desktop">
    <div class="hero-photo" role="img" aria-label="Night photograph of an off-road camper van lit from inside, parked under a starry sky beside outback trees"></div>
    <div class="site-header">
      <div class="site-logo"><span class="mark"></span><span class="name">Dune-Loop Trips</span></div>
      <nav class="site-nav">
        <a href="#">Home</a><a href="#">Tours</a><a href="#">Events</a><a href="#">Contact</a>
      </nav>
    </div>
    <div class="hero-copy">
      <p class="hero-lead">Adventure through</p>
      <h1 class="hero-title">Unbelievable locations</h1>
      <a class="btn-book" href="#">Book now
        <svg width="14" height="10" viewBox="0 0 14 10" fill="none" stroke="#fff" stroke-width="1.8"><path d="M0 5h12M8 1l4 4-4 4"/></svg>
      </a>
    </div>
  </section>

  <section class="screen screen-mobile">
    <div class="hero-photo" role="img" aria-label="Night photograph of an off-road camper van under a starry sky"></div>
    <div class="site-header">
      <div class="site-logo"><span class="mark"></span><span class="name">Dune-Loop Trips</span></div>
      <svg class="menu-toggle" viewBox="0 0 14 10" stroke="#fff" stroke-width="1.2"><path d="M0 1h14M0 5h14M0 9h14"/></svg>
    </div>
    <div class="hero-copy">
      <p class="hero-lead">Adventure through</p>
      <h1 class="hero-title">Unbelievable locations</h1>
      <a class="btn-book" href="#">Book now
        <svg width="9" height="7" viewBox="0 0 14 10" fill="none" stroke="#fff" stroke-width="2"><path d="M0 5h12M8 1l4 4-4 4"/></svg>
      </a>
    </div>
  </section>

</body>
</html>
```